zQuandaro Marketing - SEM, Influencer website. FUN RETRO VIBES.

I included content. Need an advertising website that displays, my services, blog and about me and contact.
I need to be able to easily update content, blogs by myself. Need it to be a Wordpress. I included some content pages. Please let me know if this give a better idea of what I do and the tone I am looking for.
Target Market(s)
Small Business Entrepreneurs, Start-ups, Male and Female ages 25-50
Industry/Entity Type
Advertising
Coding
Coded - Design and coding required
Number of Pages Required
3 page
Font styles to use
Other font styles liked:
- Lazer 64
Requirements
Must have
- Services, Blog, About Me, Contact. Creative Design is really what I want. Unique and fun imagery. I like the 80's style of design. Retro colors, in the logo. LAzer 84 font is cool. Hex colors should be in the brief. MUST LOOK GOOD ON MOBILE. The mobile experience has to be good.
Nice to have
- I am open minded to new creative ideas.
Hex Code
#000205
#3978A3
#5BF8FB
#7B7BFB
#5CC9EC
#AB63FA
Should not have
- Cookie Cutter feel. They made me choose the color wheel but the colors I want are on the brief. Please let me know if you need more logo images, images of me

```html
<!DOCTYPE html>
<html lang="en">
<head>
<meta charset="utf-8">
<title>zQuandaro Marketing</title>
<link href="https://fonts.googleapis.com/css2?family=Lato:ital,wght@0,400;0,700;1,400;1,700&family=Permanent+Marker&display=swap" rel="stylesheet">
<style>
:root{
  --ink:#000205;
  --brand-blue:#3978A3;
  --sky:#5CC9EC;
  --violet:#7B7BFB;
  --purple:#AB63FA;
  --text-grey:#555a60;
  --nav-grey:#5f6770;
  --white:#ffffff;
  --footer-bg:#070809;
}
*{box-sizing:border-box;margin:0;padding:0}
html,body{width:1200px;height:2514px;overflow:hidden}
body{position:relative;font-family:"Lato",sans-serif;background:var(--white);color:var(--ink)}
.abs{position:absolute}

/* header */
.site-header{left:0;top:0;width:1200px;height:88px;background:var(--white)}
.brand{left:78px;top:27px;font-family:"Lato",sans-serif;font-weight:400;font-size:29px;letter-spacing:2px;color:var(--violet);white-space:nowrap}
.main-nav{left:338px;top:38px;display:flex;gap:31px;font-size:18px;color:var(--nav-grey)}
.call-box{left:914px;top:22px;width:41px;height:41px;border-radius:7px;background:var(--sky);display:flex;align-items:center;justify-content:center}
.call-label{left:966px;top:21px;font-style:italic;font-weight:700;font-size:17px;color:var(--brand-blue)}
.call-number{left:970px;top:43px;font-size:22px;color:#444}

/* hero */
.hero{left:0;top:88px;width:1200px;height:490px;background:linear-gradient(120deg,#4a5866 0%,#6b7c8c 35%,#505e6b 60%,#3d4853 100%)}
.hero-shade{left:0;top:88px;width:1200px;height:490px;background:rgba(40,60,90,.35)}
.hero-title{left:0;top:282px;width:1200px;text-align:center;color:var(--white);font-size:34px;line-height:40px;font-weight:400}

/* headings */
.section-title{width:1200px;left:0;text-align:center;font-family:"Permanent Marker",cursive;font-size:44px;font-style:italic;letter-spacing:-1px}

/* about */
.about-copy{left:195px;top:697px;width:810px;text-align:center;font-size:14.5px;line-height:22.5px;color:var(--text-grey)}
.btn-more{left:489px;top:833px;width:224px;height:52px;border-radius:26px;background:var(--sky);box-shadow:0 4px 0 #3aa4c8;color:var(--white);font-size:20px;display:flex;align-items:center;justify-content:center}

/* services */
.services-band{left:0;top:954px;width:1200px;height:712px;background:var(--brand-blue)}
.divider-label{color:var(--white);font-size:20px;text-align:center}
.rule{height:1px;background:rgba(255,255,255,.45)}
.service{width:220px;text-align:center;color:var(--white);font-size:16px;line-height:22px}
.service svg{display:block;margin:0 auto}

/* blog */
.post-photo{width:236px;height:186px;border-radius:6px}
.post-title{width:215px;font-size:15.5px;line-height:19px;color:var(--ink)}

/* footer */
.site-footer{left:0;top:2157px;width:1200px;height:357px;background:var(--footer-bg)}
.footer-brand{left:78px;top:2196px;color:var(--white);font-size:33px;letter-spacing:2px;white-space:nowrap}
.social{width:45px;height:45px;border:1.5px solid var(--white);border-radius:50%;display:flex;align-items:center;justify-content:center}
.footer-head{color:var(--white);font-size:18px}
.footer-links{left:342px;top:2241px;color:var(--white);font-size:16px;line-height:33px;list-style:none}
.contact-item{color:#d8d8d8;font-size:13px;line-height:16px}
.contact-item b{font-weight:400;display:block;margin-bottom:5px}
.news-copy{left:858px;top:2224px;width:260px;color:#d8d8d8;font-size:12.5px;line-height:15px}
.news-input{left:860px;top:2268px;width:268px;height:36px;border:1px solid #ccc;border-radius:18px;color:#999;font-style:italic;font-size:11.5px;padding:10px 18px}
.news-btn{left:861px;top:2318px;width:138px;height:32px;border-radius:16px;background:var(--sky);box-shadow:0 3px 0 #3aa4c8;color:var(--white);font-size:13px;display:flex;align-items:center;justify-content:center}
.footer-rule{left:72px;top:2450px;width:1058px;height:1px;background:#333}
.copyright{left:0;top:2472px;width:1200px;text-align:center;color:var(--white);font-size:13px}
.copyright span{color:var(--sky)}
</style>
</head>
<body>

<header class="site-header abs"></header>
<div class="brand abs">ZQUANDARO</div>
<nav class="main-nav abs"><span>HOME</span><span>ABOUT ME</span><span>SERVICES</span><span>BLOG</span><span>CONTACT US</span></nav>
<div class="call-box abs">
  <svg width="22" height="22" viewBox="0 0 24 24"><path d="M6.6 10.8c1.4 2.8 3.8 5.1 6.6 6.6l2.2-2.2c.3-.3.7-.4 1-.2 1.1.4 2.3.6 3.6.6.6 0 1 .4 1 1V20c0 .6-.4 1-1 1C10.6 21 3 13.4 3 4c0-.6.4-1 1-1h3.5c.6 0 1 .4 1 1 0 1.3.2 2.5.6 3.6.1.3 0 .7-.2 1L6.6 10.8z" fill="#fff"/></svg>
</div>
<div class="call-label abs">CONTACT US TODAY</div>
<div class="call-number abs">23-555-0142</div>

<div class="hero abs" role="img" aria-label="Photo of a team working together at computers in a bright office"></div>
<div class="hero-shade abs"></div>
<h1 class="hero-title abs">BE A VALUABLE RESOURCE IN MY INDUSTRY,<br>THAT PRODUCES PROFITABLE RESULTS.</h1>

<h2 class="section-title abs" style="top:622px">ABOUT ME</h2>
<p class="about-copy abs">zQuandaro verb pronounced { z -kwan-dah-roh}, or digital visionary is a person who uses the Internet as a global marketplace to release their ideas, products, and services to the world. They see the digital era as an open opportunity for small business to compete with large corporations and WIN! They understand the value of digital marketing as a tool to connect people with their business. Do you see yourself as a digital visionary? I’m here to coach you through the process of upgrading your imagination and mental thought process to connect your vision with business goals.</p>
<div class="btn-more abs">Learn More</div>

<svg class="abs" style="left:0;top:936px" width="1200" height="20"><polygon points="0,0 600,18 1200,18 1200,20 0,20" fill="var(--sky)"/></svg>
<section class="services-band abs"></section>
<svg class="abs" style="left:0;top:1664px" width="1200" height="18"><polygon points="0,0 1200,0 1200,18 600,2 0,2" fill="var(--sky)"/></svg>

<h2 class="section-title abs" style="top:985px;color:var(--white)">OUR SERVICES</h2>
<div class="rule abs" style="left:80px;top:1082px;width:436px"></div>
<div class="divider-label abs" style="left:516px;top:1068px;width:168px">SEM SERVICES</div>
<div class="rule abs" style="left:694px;top:1082px;width:434px"></div>

<div class="service abs" style="left:149px;top:1150px">
  <svg width="74" height="76" viewBox="0 0 74 76" fill="none" stroke="#fff" stroke-width="3"><path d="M37 4a33 33 0 1 0 33 33"/><circle cx="37" cy="37" r="15"/><path d="M37 4v22M48 37h22M37 4a33 33 0 0 1 33 33"/></svg>
  <div style="margin-top:38px">SEARCHLY SEARCH ADS</div>
</div>
<div class="service abs" style="left:378px;top:1145px">
  <svg width="86" height="86" viewBox="0 0 86 86" fill="none" stroke="#fff" stroke-width="4"><circle cx="43" cy="43" r="40"/><ellipse cx="43" cy="43" rx="18" ry="40"/><path d="M3 43h80M43 3v80M10 22h66M10 64h66"/></svg>
  <div style="margin-top:25px">SEARCHLY DISPLAY<br>NETWORK</div>
</div>
<div class="service abs" style="left:603px;top:1153px">
  <svg width="62" height="72" viewBox="0 0 62 72" fill="none" stroke="#fff" stroke-width="2.5"><path d="M14 10h10a7 7 0 1 1 14 0h20v50H38a7 7 0 1 0-14 0H14V43a7 7 0 1 1 0-14z"/></svg>
  <div style="margin-top:30px">COMPREHENSIVE<br>RETARGETING STRATEGIES</div>
</div>
<div class="service abs" style="left:832px;top:1150px">
  <svg width="82" height="82" viewBox="0 0 82 82" fill="none" stroke="#fff" stroke-width="4"><rect x="4" y="18" width="74" height="58" rx="10"/><path d="M4 34h74M20 50h36M20 62h24"/></svg>
  <div style="margin-top:38px">FINDORA SEARCH ADS</div>
</div>

<div class="rule abs" style="left:76px;top:1368px;width:334px"></div>
<div class="divider-label abs" style="left:410px;top:1354px;width:372px">PLANNING &amp; PROPOSAL SERVICES</div>
<div class="rule abs" style="left:788px;top:1368px;width:336px"></div>

<div class="service abs" style="left:144px;top:1447px">
  <svg width="96" height="88" viewBox="0 0 96 88" fill="none" stroke="#fff" stroke-width="3"><circle cx="58" cy="38" r="32"/><circle cx="58" cy="38" r="20"/><circle cx="58" cy="38" r="8"/><path d="M34 60L8 84M40 66L14 88" /><path d="M66 46l20 14-6 6-18-16"/></svg>
  <div style="margin-top:17px">KEYWORD PLANNING</div>
</div>
<div class="service abs" style="left:372px;top:1446px">
  <svg width="100" height="78" viewBox="0 0 100 78" fill="none" stroke="#fff" stroke-width="4"><path d="M8 74V50h12v24M30 74V38h12v36M52 74V28h12v46M74 74V14h12v60"/><path d="M4 58l26-26 16 14 40-40"/><path d="M72 4h16v16"/></svg>
  <div style="margin-top:26px">COMPETITIVE ANALYSIS</div>
</div>
<div class="service abs" style="left:597px;top:1444px">
  <svg width="92" height="92" viewBox="0 0 92 92" fill="none" stroke="#fff" stroke-width="3.5"><circle cx="46" cy="46" r="38"/><path d="M46 2v14M46 76v14M2 46h14M76 46h14"/><path d="M46 70s-16-16-16-28a16 16 0 0 1 32 0c0 12-16 28-16 28z"/><circle cx="46" cy="42" r="6"/></svg>
  <div style="margin-top:22px">GEO-TARGETING</div>
</div>
<div class="service abs" style="left:827px;top:1440px">
  <svg width="90" height="96" viewBox="0 0 90 96" fill="none" stroke="#fff" stroke-width="3.5"><path d="M26 4h26l-8 18H34z"/><path d="M34 22C12 34 8 60 10 90h52c4-30-2-56-18-68"/><text x="36" y="76" font-family="Lato,sans-serif" font-size="30" font-weight="700" fill="#fff" stroke="none" text-anchor="middle">$</text><path d="M62 46l10-8 8 6"/><circle cx="84" cy="40" r="4"/></svg>
  <div style="margin-top:8px">BUDGET<br>OPPORTUNITIES AND<br>RECOMMENDATIONS</div>
</div>

<h2 class="section-title abs" style="top:1724px">OUR BLOG</h2>
<div class="post-photo abs" style="left:107px;top:1818px;background:linear-gradient(135deg,#8e9aa5,#c9ccd0 50%,#7c8b96)" role="img" aria-label="Photo of two colleagues reviewing documents at a desk"></div>
<div class="post-photo abs" style="left:357px;top:1818px;background:linear-gradient(135deg,#d7e2c8,#f4f4f2 50%,#b8c4cc)" role="img" aria-label="Photo of a woman checking her phone at a bright desk"></div>
<div class="post-photo abs" style="left:606px;top:1818px;background:linear-gradient(135deg,#6e6a66,#b9a79a 50%,#5a6b80)" role="img" aria-label="Photo of two coworkers looking at a laptop together"></div>
<div class="post-photo abs" style="left:856px;top:1818px;background:linear-gradient(135deg,#4a4d52,#c4a46a 50%,#5c8a4e)" role="img" aria-label="Photo from above of a team brainstorming around a table"></div>
<div class="post-title abs" style="left:107px;top:2022px">IT IS A LONG ESTABLISHED FACT THAT A READER.</div>
<div class="post-title abs" style="left:356px;top:2022px">IT IS A LONG ESTABLISHED FACT THAT A READER.</div>
<div class="post-title abs" style="left:609px;top:2022px">IT IS A LONG ESTABLISHED FACT THAT A READER.</div>
<div class="post-title abs" style="left:856px;top:2022px">IT IS A LONG ESTABLISHED FACT THAT A READER.</div>

<svg class="abs" style="left:0;top:2142px" width="1200" height="16"><polygon points="0,0 600,14 1200,14 1200,16 0,16" fill="var(--sky)"/></svg>
<footer class="site-footer abs"></footer>
<div class="footer-brand abs">ZQUANDARO</div>
<div class="social abs" style="left:72px;top:2280px" aria-label="Social profile link"><svg width="14" height="14" viewBox="0 0 14 14" fill="none" stroke="#fff" stroke-width="1.8"><path d="M3 11L11 3M5 3h6v6"/></svg></div>
<div class="social abs" style="left:130px;top:2280px" aria-label="Social profile link"><svg width="14" height="14" viewBox="0 0 14 14" fill="none" stroke="#fff" stroke-width="1.8"><path d="M3 11L11 3M5 3h6v6"/></svg></div>
<div class="social abs" style="left:187px;top:2280px" aria-label="Social profile link"><svg width="14" height="14" viewBox="0 0 14 14" fill="none" stroke="#fff" stroke-width="1.8"><path d="M3 11L11 3M5 3h6v6"/></svg></div>
<div class="social abs" style="left:244px;top:2280px" aria-label="Social profile link"><svg width="14" height="14" viewBox="0 0 14 14" fill="none" stroke="#fff" stroke-width="1.8"><path d="M3 11L11 3M5 3h6v6"/></svg></div>

<div class="footer-head abs" style="left:341px;top:2199px">QUICK LINKS</div>
<ul class="footer-links abs"><li>HOME</li><li>ABOUT ME</li><li>SERVICES</li><li>BLOG</li><li>CONTACT US</li></ul>

<div class="footer-head abs" style="left:557px;top:2199px">CONTACT US</div>
<svg class="abs" style="left:563px;top:2244px" width="12" height="16" viewBox="0 0 12 16"><path d="M6 0a6 6 0 0 1 6 6c0 4-6 10-6 10S0 10 0 6a6 6 0 0 1 6-6z" fill="#fff"/><circle cx="6" cy="6" r="2.2" fill="#070809"/></svg>
<div class="contact-item abs" style="left:591px;top:2238px;width:200px"><b>ADDRESS</b>All the Lorem Ipsum generators on the Internet tend</div>
<svg class="abs" style="left:562px;top:2308px" width="15" height="15" viewBox="0 0 24 24"><path d="M6.6 10.8c1.4 2.8 3.8 5.1 6.6 6.6l2.2-2.2c.3-.3.7-.4 1-.2 1.1.4 2.3.6 3.6.6.6 0 1 .4 1 1V20c0 .6-.4 1-1 1C10.6 21 3 13.4 3 4c0-.6.4-1 1-1h3.5c.6 0 1 .4 1 1 0 1.3.2 2.5.6 3.6.1.3 0 .7-.2 1z" fill="#fff"/></svg>
<div class="contact-item abs" style="left:592px;top:2306px"><b>PHONE</b>23-555-0142</div>
<svg class="abs" style="left:566px;top:2360px" width="14" height="10" viewBox="0 0 14 10"><rect width="14" height="10" rx="1" fill="#fff"/><path d="M0 1l7 5 7-5" fill="none" stroke="#070809" stroke-width="1.2"/></svg>
<div class="contact-item abs" style="left:592px;top:2357px"><b>EMAIL ADDRESS</b>info@zquandaroworld.test</div>

<div class="footer-head abs" style="left:858px;top:2199px">SUBSCRIBE OUR NEWSLETTER</div>
<p class="news-copy abs">If you are going to use a passage of Lorem Ipsum, you need to be sure</p>
<div class="news-input abs">enter your email here. . .</div>
<div class="news-btn abs">Subscribe</div>

<div class="footer-rule abs"></div>
<div class="copyright abs">© 2020 <span>zquandaroworld</span>.All Right Reserved</div>

</body>
</html>
```